Design Card that Captures Life's Moments

Thinking black and white design with maybe some accent colors. Open to others too. Looking for bold and modern to accompany new logo design. For the side without my info, would have tagline of "Capturing Life's Moments" with either logo or website petravossimaging.com. I want the tagline to dominate and be the main focus of that side.

Target Market(s)

Something that can appeal to people who might be interested in family/kids, business, sports, commercial, or birth/newborn photography.

Industry/Entity Type

Professional Photography

Contact Information for Business Card

Font styles to use
Sans Serif
Script
Other font styles liked:
• Go with Logo, but the tagline could be script that popped.

Requirements
Must have
• See details above! Wow factor! Make someone pick my card up and take it home or at least to look at it further.
• Tagline: Capturing Life's Moments (Main text on side without name)
• INFO:
• Petra Voss-Hale - Photographer
• 555-318-0462 - Cell and for SMS
• www.petravossimaging.com - Website (maybe on side with tagline?)
• petra@petrastudioframes.com - Email
Nice to have
• JUST AN IDEA... I would like to see Capturing Life's Moment really take over most of one side of the card. Think greeting card. Where you can't miss it. It is in your face, but nice and elegant. Maybe cursive, but could work with other font. Instead of logo on tagline side, just have petravossimaging.com in smaller text along one of the edges.
Should not have
• Too simple I could of created it, like with only my logo and some typed text.

```html
<!DOCTYPE html>
<html lang="en">
<head>
<meta charset="utf-8">
<title>Petra Voss Imaging – Business Card</title>
<link rel="stylesheet" href="https://fonts.googleapis.com/css2?family=Questrial&display=swap">
<style>
  :root {
    --backdrop: #a29f98;
    --ink-black: #0b0b0b;
    --charcoal: #2a2a2a;
    --slate: #5a5a5a;
    --band-grey: #8a8a8a;
    --sepia-light: #e8e0d2;
    --sepia-mid: #b9aa92;
    --sepia-dark: #6e604e;
    --tan: #a8957a;
    --paper: #f4f2ee;
    --text-light: #f1f1f1;
    --text-soft: #e4e4e4;
  }
  * { box-sizing: border-box; margin: 0; padding: 0; }
  html, body { width: 1200px; height: 940px; overflow: hidden; }
  body {
    background: var(--backdrop);
    font-family: "Questrial", "Century Gothic", sans-serif;
    display: flex;
    flex-direction: column;
    align-items: center;
    justify-content: center;
    gap: 40px;
  }
  .card {
    position: relative;
    width: 700px;
    height: 400px;
    overflow: hidden;
    box-shadow: 0 6px 18px rgba(0,0,0,0.25);
  }
  .card-shapes, .card-photo { position: absolute; inset: 0; width: 100%; height: 100%; }

  /* Tagline side */
  .card--tagline { background: var(--ink-black); }
  .brand {
    position: absolute;
    left: 34px;
    top: 30px;
    color: var(--text-light);
    line-height: 1;
  }
  .brand-name { font-size: 24px; letter-spacing: 1px; }
  .brand-sub {
    margin-left: 8px;
    font-size: 24px;
    letter-spacing: 1px;
  }
  .tagline {
    position: absolute;
    left: 34px;
    top: 112px;
    color: var(--text-light);
    font-size: 52px;
    line-height: 1.12;
  }
  .tagline-line { display: block; }
  .website {
    position: absolute;
    left: 34px;
    top: 256px;
    color: var(--text-light);
    font-size: 16px;
    letter-spacing: 0.5px;
  }

  /* Contact side */
  .card--contact { background: var(--charcoal); }
  .name-band {
    position: absolute;
    left: 150px;
    top: 58px;
    width: 340px;
    color: var(--text-light);
  }
  .name-band-accent {
    position: absolute;
    left: -18px;
    top: 0;
    width: 18px;
    height: 44px;
    background: var(--tan);
  }
  .person-name {
    display: block;
    background: var(--band-grey);
    font-size: 26px;
    line-height: 44px;
    padding-left: 14px;
  }
  .person-role {
    display: block;
    background: var(--slate);
    font-size: 20px;
    line-height: 34px;
    padding-left: 14px;
    color: var(--text-soft);
  }
  .contact-list {
    position: absolute;
    left: 36px;
    top: 178px;
    list-style: none;
    color: var(--text-light);
    font-size: 20px;
  }
  .contact-item {
    display: flex;
    align-items: center;
    gap: 14px;
    height: 40px;
  }
  .contact-icon { width: 22px; height: 22px; flex: none; }
</style>
</head>
<body>

  <!-- Tagline side -->
  <section class="card card--tagline">
    <svg class="card-shapes" viewBox="0 0 700 400" aria-hidden="true">
      <polygon points="230,400 700,104 700,128 268,400" fill="var(--band-grey)"/>
    </svg>
    <svg class="card-photo" viewBox="0 0 700 400" role="img" aria-label="Sepia portrait photograph of a woman in a beaded strapless gown">
      <defs>
        <linearGradient id="sepiaTagline" x1="0" y1="0" x2="1" y2="1">
          <stop offset="0" stop-color="var(--sepia-light)"/>
          <stop offset="0.55" stop-color="var(--sepia-mid)"/>
          <stop offset="1" stop-color="var(--sepia-dark)"/>
        </linearGradient>
      </defs>
      <polygon points="296,400 700,146 700,400" fill="url(#sepiaTagline)"/>
    </svg>
    <div class="brand">
      <span class="brand-name">Petra Voss</span><span class="brand-sub">Photography</span>
    </div>
    <h1 class="tagline">
      <span class="tagline-line">Capturing</span>
      <span class="tagline-line">Life's Moments</span>
    </h1>
    <p class="website">www.petravossimaging.com</p>
  </section>

  <!-- Contact side -->
  <section class="card card--contact">
    <svg class="card-photo" viewBox="0 0 700 400" role="img" aria-label="Sepia portrait photograph of a woman in a beaded strapless gown">
      <defs>
        <linearGradient id="sepiaContact" x1="0" y1="0" x2="1" y2="1">
          <stop offset="0" stop-color="var(--sepia-light)"/>
          <stop offset="0.55" stop-color="var(--sepia-mid)"/>
          <stop offset="1" stop-color="var(--sepia-dark)"/>
        </linearGradient>
      </defs>
      <polygon points="150,400 700,92 700,400" fill="url(#sepiaContact)"/>
      <line x1="150" y1="400" x2="700" y2="92" stroke="var(--paper)" stroke-width="4"/>
    </svg>
    <div class="name-band">
      <span class="name-band-accent"></span>
      <span class="person-name">Petra Voss-Hale</span>
      <span class="person-role">Photographer</span>
    </div>
    <ul class="contact-list">
      <li class="contact-item">
        <svg class="contact-icon" viewBox="0 0 22 22" aria-hidden="true">
          <rect width="22" height="22" rx="4" fill="var(--tan)"/>
          <rect x="7" y="4" width="8" height="14" rx="1.5" fill="none" stroke="var(--ink-black)" stroke-width="1.6"/>
          <circle cx="11" cy="15.5" r="0.9" fill="var(--ink-black)"/>
        </svg>
        <span>555-318-0462</span>
      </li>
      <li class="contact-item">
        <svg class="contact-icon" viewBox="0 0 22 22" aria-hidden="true">
          <rect width="22" height="22" rx="4" fill="var(--tan)"/>
          <rect x="4" y="6.5" width="14" height="9" fill="none" stroke="var(--ink-black)" stroke-width="1.5"/>
          <polyline points="4,6.5 11,12 18,6.5" fill="none" stroke="var(--ink-black)" stroke-width="1.5"/>
        </svg>
        <span>petra@petrastudioframes.com</span>
      </li>
    </ul>
  </section>

</body>
</html>
```